Bref créative
Business Cards & Stationary For Law Firm - Use Existing Logo
Harlow Law Offices
I need double sided standard sized Business Card [3.5" x 2"]
I am open to different fonts for the info. I have used Century Gothic before but try any
Professional
Dorian P. Harlow, Esq.
482 N.E. 3rd Avenue
Suite 2206
Miami, Florida 33130
dph@harlowlo.example
www.harlowlo.example
To me the most important thing on a card is that they get your information quickly and easily. I see so many cards that are unmemorable and cluttered with tiny type. I think people want your name and phone easy to read and accessible.
Can put logo and/or any information on either side. Try different designs.

```html
<!DOCTYPE html>
<html lang="en">
<head>
<meta charset="utf-8">
<title>Harlow Law Offices — Business Card</title>
<link href="https://fonts.googleapis.com/css2?family=Cinzel:wght@400;600&family=Cormorant+Garamond:wght@500&display=swap" rel="stylesheet">
<style>
  :root {
    --page: #d9dadc;
    --card-white: #ffffff;
    --brand-blue: #1f5fd6;
    --brand-blue-deep: #0d3fae;
    --brand-blue-light: #4a86f0;
    --navy: #0e1f4d;
    --ink: #2b2f38;
    --ink-soft: #6a6f7a;
    --rule: #b9bec8;
    --black: #0b0c10;
  }
  * { box-sizing: border-box; margin: 0; padding: 0; }
  html, body { width: 1200px; height: 895px; overflow: hidden; }
  body {
    background: var(--page);
    display: flex;
    align-items: center;
    justify-content: center;
    gap: 40px;
    font-family: "Cormorant Garamond", Georgia, serif;
  }
  .card {
    position: relative;
    width: 540px;
    height: 309px;
    overflow: hidden;
    box-shadow: 0 10px 26px rgba(0,0,0,0.18);
  }

  /* Front */
  .card--front { background: var(--card-white); }
  .brand {
    position: absolute;
    top: 50px; left: 0; right: 0;
    display: flex; align-items: center; justify-content: center; gap: 14px;
  }
  .brand__mark {
    width: 30px; height: 30px;
    background: var(--brand-blue);
  }
  .brand__name {
    font-family: "Cinzel", Georgia, serif;
    font-weight: 600;
    font-size: 24px;
    letter-spacing: 1px;
    color: var(--brand-blue-deep);
  }
  .details {
    position: absolute;
    top: 130px; left: 46px; right: 46px;
    display: flex;
  }
  .details__person { width: 54%; padding-right: 18px; }
  .details__contact {
    flex: 1;
    padding-left: 20px;
    border-left: 1px solid var(--rule);
  }
  .person__name {
    font-family: "Cinzel", Georgia, serif;
    font-size: 14px;
    color: var(--brand-blue-deep);
    margin-bottom: 8px;
  }
  .person__address {
    font-size: 11.5px;
    line-height: 1.45;
    color: var(--ink-soft);
    font-style: normal;
  }
  .contact__row {
    display: flex; align-items: center; gap: 8px;
    font-size: 11.5px; line-height: 1.55;
    color: var(--ink);
  }
  .contact__icon { width: 10px; height: 10px; flex: none; }
  .front-band { position: absolute; left: 0; bottom: 0; width: 540px; height: 70px; }

  /* Back */
  .card--back {
    background: radial-gradient(ellipse at 60% 40%, var(--brand-blue-light) 0%, var(--brand-blue) 45%, var(--brand-blue-deep) 100%);
  }
  .back-brand {
    position: absolute; inset: 0;
    display: flex; align-items: center; justify-content: center; gap: 14px;
  }
  .back-brand .brand__mark { background: var(--navy); width: 34px; height: 34px; }
  .back-brand .brand__name { color: var(--navy); font-size: 26px; }
  .back-url {
    position: absolute;
    left: 22px; top: 50%;
    transform: translate(-50%, -50%) rotate(-90deg);
    transform-origin: center;
    margin-left: 10px;
    font-family: "Cinzel", Georgia, serif;
    font-size: 10px;
    letter-spacing: 4px;
    color: rgba(255,255,255,0.85);
    white-space: nowrap;
  }
</style>
</head>
<body>

  <section class="card card--front" aria-label="Business card front">
    <div class="brand">
      <span class="brand__mark"></span>
      <span class="brand__name">Harlow Law Offices</span>
    </div>

    <div class="details">
      <div class="details__person">
        <p class="person__name">Dorian P. Harlow, Esq.</p>
        <address class="person__address">
          482 N.E. 3rd Avenue, Suite 2206<br>
          Miami, Florida 33130
        </address>
      </div>
      <div class="details__contact">
        <p class="contact__row">
          <svg class="contact__icon" viewBox="0 0 10 10"><path d="M2 1 L4 1 L4.6 3 L3.4 4 Q4.5 6 6 6.6 L7 5.4 L9 6 L9 8 Q5 9 2.5 6.5 Q1 4.5 2 1Z" fill="var(--brand-blue)"/></svg>
          (305) 555-0142
        </p>
        <p class="contact__row">
          <svg class="contact__icon" viewBox="0 0 10 10"><rect x="1" y="3" width="8" height="5" fill="var(--brand-blue)"/><rect x="3" y="1" width="4" height="2" fill="var(--brand-blue)"/></svg>
          (305) 555-0143
        </p>
        <p class="contact__row">
          <svg class="contact__icon" viewBox="0 0 10 10"><rect x="1" y="2" width="8" height="6" fill="var(--brand-blue)"/><path d="M1 2 L5 5.5 L9 2" stroke="#fff" stroke-width="0.9" fill="none"/></svg>
          dph@harlowlo.example
        </p>
        <p class="contact__row">
          <svg class="contact__icon" viewBox="0 0 10 10"><circle cx="5" cy="5" r="4" fill="var(--brand-blue)"/><path d="M1 5 H9 M5 1 Q2.5 5 5 9 M5 1 Q7.5 5 5 9" stroke="#fff" stroke-width="0.6" fill="none"/></svg>
          www.harlowlo.example
        </p>
      </div>
    </div>

    <svg class="front-band" viewBox="0 0 540 70" preserveAspectRatio="none" aria-hidden="true">
      <defs>
        <linearGradient id="bandBlue" x1="0" y1="0" x2="1" y2="0">
          <stop offset="0" stop-color="var(--brand-blue-deep)"/>
          <stop offset="1" stop-color="var(--brand-blue-light)"/>
        </linearGradient>
      </defs>
      <polygon points="0,38 330,38 360,70 0,70" fill="url(#bandBlue)"/>
      <polygon points="360,70 330,38 540,14 540,70" fill="var(--black)"/>
    </svg>
  </section>

  <section class="card card--back" aria-label="Business card back">
    <div class="back-brand">
      <span class="brand__mark"></span>
      <span class="brand__name">Harlow Law Offices</span>
    </div>
    <p class="back-url">www.harlowlo.example</p>
  </section>

</body>
</html>
```